Strategic design partner needed for newly global technical consultancy! Starting with PowerPoint!

Veltrano.biz is a new consulting company offering technical assurance (reliability, business and cyber resiliency, operational excellence, and technical agility). We already have a logo (attached) and main font (Montserrat). Our colour scheme is gold and charcoal (color code of charcoal is #36454F, and for the gold is #B69904).
See the attachment for full colour palette we want! We need to partner with a designer for our corporate branding, starting with a PowerPoint deck that will be used for proposals and client meetings.
In a proposal deck we have items like Problem Statement (our joint understanding), Our Approach, Architecture, Timeline, Team, Assumptions/Dependencies/Risks, RACI, Pricing.
For corporate presentations we would have Introduction, Services, Methodology, Case Studies, Team, Clients, Contact.
This could lead to much more work. The website is just a placeholder, but we like the colours (veltrano dot biz)

Industry/Entity Type

Technology solutions apply across all industries. We have clients in fintech, pharma, retail, etc.

Requirements
Must have
• Match the colour scheme - SEE UPLOADED ATTACHMENT

```html
<!DOCTYPE html>
<html lang="en">
<head>
<meta charset="utf-8">
<title>Veltrano – Proposal Deck Templates</title>
<link href="https://fonts.googleapis.com/css2?family=Montserrat:wght@300;400;500;600;700&display=swap" rel="stylesheet">
<style>
  :root{
    --charcoal:#36454F;
    --gold:#B69904;
    --gold-soft:#d8c98a;
    --paper:#ffffff;
    --slide-a:#efefef;
    --slide-b:#dcdcdc;
    --text:#4a4f55;
    --muted:#6b7176;
    --red:#e02020;
    --green:#5aa832;
    --amber:#f0b400;
    --blue:#4a8fd8;
    --grey:#777;
  }
  *{margin:0;padding:0;box-sizing:border-box}
  html,body{width:1200px;height:1200px;overflow:hidden;background:var(--paper)}
  body{position:relative;font-family:'Montserrat',sans-serif;color:var(--text)}
  .slide{position:absolute;width:537px;height:302px;overflow:hidden;
    background:linear-gradient(135deg,var(--slide-a),var(--slide-b))}
  .s1{left:44px;top:56px;background:linear-gradient(90deg,#fff 0%,#f1f1f1 60%,#e4e4e4 100%)}
  .s2{left:626px;top:56px}
  .s3{left:44px;top:453px}
  .s4{left:626px;top:453px}
  .s5{left:44px;top:849px}
  .s6{left:626px;top:849px}
  .a{position:absolute}
  .bar{position:absolute;left:0;top:0;width:8px;height:302px;
    background:linear-gradient(var(--charcoal) 0 151px,var(--gold) 151px 302px)}
  .s1 .bar{width:19px}
  .slide-title{position:absolute;left:28px;top:16px;font-weight:300;font-size:21px;color:var(--charcoal);letter-spacing:.2px}
  .footer-line{position:absolute;left:28px;right:68px;top:288px;height:1px;background:var(--gold-soft)}
  .footer-text{position:absolute;left:28px;top:291px;font-size:4px;color:var(--charcoal)}
  .brand{position:absolute;right:17px;top:285px;display:flex;flex-direction:column;align-items:center;gap:1px;
    font-size:6.5px;font-weight:700;color:var(--charcoal);letter-spacing:.2px}
  .brand i{display:block;width:6px;height:6px;background:var(--charcoal)}
  .label{font-size:9px;font-weight:700;color:var(--gold);text-transform:uppercase;white-space:nowrap}
  .body{font-size:6.7px;line-height:8.8px;color:var(--text);text-align:center}
  .photo{position:absolute}

  /* cover */
  .confidential{left:22px;top:3px;font-size:3.5px;color:var(--muted)}
  .cover-photo{left:300px;top:0;width:237px;height:302px;
    background:linear-gradient(90deg,rgba(255,255,255,0),rgba(150,150,150,.55) 40%,rgba(70,70,70,.65) 75%,rgba(180,180,180,.5))}
  .cover-brand{left:40px;top:112px;display:flex;align-items:center;gap:6px;font-size:20px;font-weight:700;color:var(--charcoal);letter-spacing:.3px}
  .cover-brand i{display:block;width:14px;height:14px;background:var(--gold)}
  .cover-title{left:39px;top:172px;font-size:24px;font-weight:400;color:var(--charcoal);letter-spacing:.3px}
  .cover-sub{left:40px;top:206px;font-size:10px;color:var(--charcoal)}
  .cover-date{left:40px;top:253px;font-size:10px;color:var(--charcoal)}
  .cover-date sup{font-size:6px}

  /* contents */
  .stairs{left:8px;top:0;width:201px;height:302px;
    background:linear-gradient(160deg,#b9b2a8 0%,#d6d3cf 35%,#9aa6a0 60%,#4f6a62 80%,#e3e3e1 100%)}
  .s2 .slide-title{z-index:2}
  .toc{position:absolute;left:199px;top:57px;list-style:none}
  .toc li{display:flex;align-items:center;height:28.7px;gap:8px}
  .toc svg{width:22px;height:20px}
  .toc span{font-size:9px;font-weight:700;color:var(--gold)}
  .s2 .footer-line{left:212px}

  /* approach */
  .step{position:absolute;top:64px;width:90px;margin-left:-45px;display:flex;flex-direction:column;align-items:center}
  .step svg{width:94px;height:120px;margin-top:-14px}
  .step .label{margin-top:-2px}
  .step .body{margin-top:5px;width:72px}

  /* problem */
  .point{position:absolute;width:120px;margin-left:-60px;display:flex;flex-direction:column;align-items:center}
  .point svg{width:28px;height:28px}
  .point .label{margin-top:4px}
  .point .body{margin-top:3px;width:118px}

  /* team */
  .member{position:absolute;top:69px;width:130px;margin-left:-65px;display:flex;flex-direction:column;align-items:center}
  .avatar{width:44px;height:42px;background:linear-gradient(#f4f4f4,#b5b9bd);border:1px solid #e6e2d0}
  .member .label{margin-top:15px}
  .member .body{margin-top:6px;width:128px}
  .member .body p+p{margin-top:3px}

  /* risks */
  .col{position:absolute;top:54px;left:0;width:106px;display:flex;flex-direction:column;align-items:center}
  .col svg{width:30px;height:30px}
  .col .label{margin-top:2px;padding-bottom:3px;width:100%;text-align:center;border-bottom:1px solid var(--gold-soft)}
  .rows{width:100%;list-style:none;margin-top:1px}
  .rows li{display:flex;align-items:center;height:16.6px;font-size:6.5px;color:var(--text);border-bottom:1px solid #e4e4e4}
  .rows li b{font-weight:400;flex:1}
  .rows li i{width:3px;height:3px;border-radius:50%;margin-right:26px}
  .rows li em{font-style:normal;width:4px;text-align:right}
  .note{margin-top:4px;width:100%;height:76px;background:var(--charcoal);color:#fff;font-size:6.5px;line-height:8px;
    text-align:center;display:flex;align-items:center;justify-content:center;padding:0 5px}
</style>
</head>
<body>

<!-- Cover -->
<section class="slide s1">
  <div class="bar"></div>
  <div class="a confidential">CONFIDENTIAL</div>
  <div class="photo cover-photo" role="img" aria-label="Black and white photograph of a modern steel-framed building reflected in still water"></div>
  <div class="a cover-brand"><i></i>VELTRANO</div>
  <div class="a cover-title">PRESENTATION TITLE</div>
  <div class="a cover-sub">Presentation Sub-Title</div>
  <div class="a cover-date">28<sup>th</sup> February 2023</div>
</section>

<!-- Contents -->
<section class="slide s2">
  <div class="bar"></div>
  <div class="photo stairs" role="img" aria-label="Photograph of a white staircase with dark green treads"></div>
  <div class="slide-title">Content</div>
  <ol class="toc">
    <li><svg viewBox="0 0 22 20"><polygon points="5.5,0 16.5,0 22,10 16.5,20 5.5,20 0,10" fill="var(--gold)"/><text x="11" y="13.5" font-size="9" font-weight="700" fill="#fff" text-anchor="middle" font-family="Montserrat,sans-serif">1</text></svg><span>PROBLEM STATEMENT</span></li>
    <li><svg viewBox="0 0 22 20"><polygon points="5.5,0 16.5,0 22,10 16.5,20 5.5,20 0,10" fill="var(--gold)"/><text x="11" y="13.5" font-size="9" font-weight="700" fill="#fff" text-anchor="middle" font-family="Montserrat,sans-serif">2</text></svg><span>OUR APPROACH</span></li>
    <li><svg viewBox="0 0 22 20"><polygon points="5.5,0 16.5,0 22,10 16.5,20 5.5,20 0,10" fill="var(--gold)"/><text x="11" y="13.5" font-size="9" font-weight="700" fill="#fff" text-anchor="middle" font-family="Montserrat,sans-serif">3</text></svg><span>ARCHITECTURE</span></li>
    <li><svg viewBox="0 0 22 20"><polygon points="5.5,0 16.5,0 22,10 16.5,20 5.5,20 0,10" fill="var(--gold)"/><text x="11" y="13.5" font-size="9" font-weight="700" fill="#fff" text-anchor="middle" font-family="Montserrat,sans-serif">4</text></svg><span>TIMELINE</span></li>
    <li><svg viewBox="0 0 22 20"><polygon points="5.5,0 16.5,0 22,10 16.5,20 5.5,20 0,10" fill="var(--gold)"/><text x="11" y="13.5" font-size="9" font-weight="700" fill="#fff" text-anchor="middle" font-family="Montserrat,sans-serif">5</text></svg><span>TEAM</span></li>
    <li><svg viewBox="0 0 22 20"><polygon points="5.5,0 16.5,0 22,10 16.5,20 5.5,20 0,10" fill="var(--gold)"/><text x="11" y="13.5" font-size="9" font-weight="700" fill="#fff" text-anchor="middle" font-family="Montserrat,sans-serif">6</text></svg><span>ASSUMPTIONS/DEPENDENCIES AND RISKS</span></li>
    <li><svg viewBox="0 0 22 20"><polygon points="5.5,0 16.5,0 22,10 16.5,20 5.5,20 0,10" fill="var(--gold)"/><text x="11" y="13.5" font-size="9" font-weight="700" fill="#fff" text-anchor="middle" font-family="Montserrat,sans-serif">7</text></svg><span>RACI</span></li>
    <li><svg viewBox="0 0 22 20"><polygon points="5.5,0 16.5,0 22,10 16.5,20 5.5,20 0,10" fill="var(--gold)"/><text x="11" y="13.5" font-size="9" font-weight="700" fill="#fff" text-anchor="middle" font-family="Montserrat,sans-serif">8</text></svg><span>PRICING</span></li>
  </ol>
  <div class="footer-line"></div>
  <div class="footer-text">Presentation Title | 2</div>
  <div class="brand"><i></i>VELTRANO</div>
</section>

<!-- Our Approach -->
<section class="slide s3">
  <div class="bar"></div>
  <div class="slide-title">Our Approach</div>

  <div class="step" style="left:92px">
    <svg viewBox="0 0 94 120"><path d="M3 50 A44 44 0 0 0 47 94" fill="none" stroke="var(--gold-soft)" stroke-width=".6"/><circle cx="47" cy="50" r="36" fill="var(--gold)"/><circle cx="47" cy="112" r="1.6" fill="var(--gold)"/>
      <g fill="none" stroke="#fff" stroke-width="2"><circle cx="52" cy="44" r="13"/><line x1="43" y1="53" x2="30" y2="66" stroke-width="4"/><ellipse cx="52" cy="44" rx="7" ry="4"/><circle cx="52" cy="44" r="1.5" fill="#fff"/></g></svg>
    <div class="label">Discovery</div>
    <div class="body">Lorem ipsum dolor sit amet, consectetur adipiscing elit, sed do eiusmod tempor incididunt ut labore et dolore magna aliqua.</div>
  </div>
  <div class="step" style="left:184px">
    <svg viewBox="0 0 94 120"><path d="M3 50 A44 44 0 0 1 47 6" fill="none" stroke="var(--gold-soft)" stroke-width=".6"/><path d="M91 50 A44 44 0 0 0 47 6" fill="none" stroke="var(--gold-soft)" stroke-width=".6"/><circle cx="47" cy="50" r="36" fill="var(--gold)"/><circle cx="47" cy="112" r="1.6" fill="var(--gold)"/>
      <g fill="none" stroke="#fff" stroke-width="1.8"><rect x="33" y="30" width="28" height="36" rx="2"/><rect x="41" y="27" width="12" height="5"/><circle cx="40" cy="58" r="2.5"/><circle cx="52" cy="48" r="2.5"/><path d="M42 56 L50 50 M54 46 L55 38 M40 42 h4 M42 40 v4"/></g></svg>
    <div class="label">Strategy</div>
    <div class="body">Lorem ipsum dolor sit amet, consectetur adipiscing elit, sed do eiusmod tempor incididunt ut labore et dolore magna aliqua.</div>
  </div>
  <div class="step" style="left:277px">
    <svg viewBox="0 0 94 120"><path d="M3 50 A44 44 0 0 0 47 94" fill="none" stroke="var(--gold-soft)" stroke-width=".6"/><circle cx="47" cy="50" r="36" fill="var(--gold)"/><circle cx="47" cy="112" r="1.6" fill="var(--gold)"/>
      <g fill="none" stroke="#fff" stroke-width="1.8"><path d="M30 66 h34 M32 66 v-10 h28 v10 M36 56 v-10 l10-14 l5 4"/><rect x="50" y="50" width="10" height="6"/></g></svg>
    <div class="label">Production</div>
    <div class="body">Lorem ipsum dolor sit amet, consectetur adipiscing elit, sed do eiusmod tempor incididunt ut labore et dolore magna aliqua.</div>
  </div>
  <div class="step" style="left:370px">
    <svg viewBox="0 0 94 120"><path d="M3 50 A44 44 0 0 1 47 6" fill="none" stroke="var(--gold-soft)" stroke-width=".6"/><path d="M91 50 A44 44 0 0 0 47 6" fill="none" stroke="var(--gold-soft)" stroke-width=".6"/><circle cx="47" cy="50" r="36" fill="var(--gold)"/><circle cx="47" cy="112" r="1.6" fill="var(--gold)"/>
      <g fill="none" stroke="#fff" stroke-width="1.8"><circle cx="44" cy="50" r="14" stroke-dasharray="5 3" stroke-width="4"/><circle cx="44" cy="50" r="7"/><path d="M48 46 h16 l-3-3 M48 54 h16 l-3 3"/></g></svg>
    <div class="label">Implementation</div>
    <div class="body">Lorem ipsum dolor sit amet, consectetur adipiscing elit, sed do eiusmod tempor incididunt ut labore et dolore magna aliqua.</div>
  </div>
  <div class="step" style="left:465px">
    <svg viewBox="0 0 94 120"><path d="M91 50 A44 44 0 0 1 47 94" fill="none" stroke="var(--gold-soft)" stroke-width=".6"/><circle cx="47" cy="50" r="36" fill="var(--gold)"/><circle cx="47" cy="112" r="1.6" fill="var(--gold)"/>
      <g fill="none" stroke="#fff" stroke-width="1.8"><rect x="41" y="30" width="12" height="12"/><rect x="32" y="42" width="14" height="14"/><rect x="48" y="42" width="14" height="14"/><path d="M30 60 h34 M33 60 v3 M61 60 v3"/></g></svg>
    <div class="label">Final Product</div>
    <div class="body">Lorem ipsum dolor sit amet, consectetur adipiscing elit, sed do eiusmod tempor incididunt ut labore et dolore magna aliqua.</div>
  </div>

  <div class="footer-line"></div>
  <div class="footer-text">Presentation Title | 2</div>
  <div class="brand"><i></i>VELTRANO</div>
</section>

<!-- Problem Statement -->
<section class="slide s4">
  <div class="bar"></div>
  <div class="slide-title">Problem Statement</div>

  <div class="point" style="left:92px;top:67px">
    <svg viewBox="0 0 28 28"><circle cx="14" cy="14" r="14" fill="var(--gold)"/><g fill="none" stroke="#fff" stroke-width="1"><circle cx="14" cy="11" r="4"/><path d="M7 22 q7-8 14 0"/></g></svg>
    <div class="label">Situation</div>
    <div class="body">Lorem ipsum dolor sit amet, consectetur adipiscing elit, sed do eiusmod tempor incididunt ut labore et dolore magna aliqua.</div>
  </div>
  <div class="point" style="left:268px;top:67px">
    <svg viewBox="0 0 28 28"><circle cx="14" cy="14" r="14" fill="var(--gold)"/><g fill="none" stroke="#fff" stroke-width="1"><rect x="7" y="7" width="14" height="14"/><path d="M10 18 v-8 h8 v6 h-5 v-3 h2"/></g></svg>
    <div class="label">Complication</div>
    <div class="body">Lorem ipsum dolor sit amet, consectetur adipiscing elit, sed do eiusmod tempor incididunt ut labore et dolore magna aliqua.</div>
  </div>
  <div class="point" style="left:444px;top:67px">
    <svg viewBox="0 0 28 28"><circle cx="14" cy="14" r="14" fill="var(--gold)"/><g fill="none" stroke="#fff" stroke-width="1"><circle cx="14" cy="8" r="2"/><circle cx="8" cy="18" r="2"/><circle cx="20" cy="18" r="2"/><path d="M14 10 v4 M14 14 L9 16 M14 14 L19 16"/></g></svg>
    <div class="label">Stakeholders</div>
    <div class="body">Lorem ipsum dolor sit amet, consectetur adipiscing elit, sed do eiusmod tempor incididunt ut labore et dolore magna aliqua.</div>
  </div>
  <div class="point" style="left:92px;top:176px">
    <svg viewBox="0 0 28 28"><circle cx="14" cy="14" r="14" fill="var(--gold)"/><g fill="none" stroke="#fff" stroke-width="1"><rect x="8" y="7" width="12" height="14"/><path d="M10 11 h8 M10 14 h8 M10 17 h5"/></g></svg>
    <div class="label">Problem Statement</div>
    <div class="body">Lorem ipsum dolor sit amet, consectetur adipiscing elit, sed do eiusmod tempor incididunt ut labore et dolore magna aliqua.</div>
  </div>
  <div class="point" style="left:268px;top:176px">
    <svg viewBox="0 0 28 28"><circle cx="14" cy="14" r="14" fill="var(--gold)"/><g fill="none" stroke="#fff" stroke-width="1"><circle cx="14" cy="14" r="7"/><circle cx="14" cy="14" r="3"/><path d="M14 5 v4 M14 19 v4 M5 14 h4 M19 14 h4"/></g></svg>
    <div class="label">Scope</div>
    <div class="body">Lorem ipsum dolor sit amet, consectetur adipiscing elit, sed do eiusmod tempor incididunt ut labore et dolore magna aliqua.</div>
  </div>
  <div class="point" style="left:444px;top:176px">
    <svg viewBox="0 0 28 28"><circle cx="14" cy="14" r="14" fill="var(--gold)"/><g fill="none" stroke="#fff" stroke-width="1"><rect x="6" y="8" width="16" height="11"/><path d="M11 22 h6 M14 19 v3 M9 16 v-2 M12 16 v-4 M15 16 v-3 M18 16 v-5"/></g></svg>
    <div class="label">Hypotheses</div>
    <div class="body">Lorem ipsum dolor sit amet, consectetur adipiscing elit, sed do eiusmod tempor incididunt ut labore et dolore magna aliqua.</div>
  </div>

  <div class="footer-line"></div>
  <div class="footer-text">Presentation Title | 2</div>
  <div class="brand"><i></i>VELTRANO</div>
</section>

<!-- Our Team -->
<section class="slide s5">
  <div class="bar"></div>
  <div class="slide-title">Our Team</div>

  <div class="member" style="left:112px">
    <div class="avatar" role="img" aria-label="Team member portrait placeholder"></div>
    <div class="label">Mr. Lorem Ipsum Dolor</div>
    <div class="body"><p>Lorem ipsum dolor sit amet, consectetur adipiscing elit, sed do eiusmod tempor incididunt ut labore et dolore magna aliqua.</p><p>Lorem ipsum dolor sit amet, consectetur adipiscing elit, sed do eiusmod tempor incididunt ut labore et dolore magna aliqua.</p><p>Lorem ipsum dolor sit amet, consectetur adipiscing elit, sed do eiusmod tempor incididunt ut labore et dolore magna aliqua.</p></div>
  </div>
  <div class="member" style="left:279px">
    <div class="avatar" role="img" aria-label="Team member portrait placeholder"></div>
    <div class="label">Mr. Lorem Ipsum Dolor</div>
    <div class="body"><p>Lorem ipsum dolor sit amet, consectetur adipiscing elit, sed do eiusmod tempor incididunt ut labore et dolore magna aliqua.</p><p>Lorem ipsum dolor sit amet, consectetur adipiscing elit, sed do eiusmod tempor incididunt ut labore et dolore magna aliqua.</p><p>Lorem ipsum dolor sit amet, consectetur adipiscing elit, sed do eiusmod tempor incididunt ut labore et dolore magna aliqua.</p></div>
  </div>
  <div class="member" style="left:445px">
    <div class="avatar" role="img" aria-label="Team member portrait placeholder"></div>
    <div class="label">Mr. Lorem Ipsum Dolor</div>
    <div class="body"><p>Lorem ipsum dolor sit amet, consectetur adipiscing elit, sed do eiusmod tempor incididunt ut labore et dolore magna aliqua.</p><p>Lorem ipsum dolor sit amet, consectetur adipiscing elit, sed do eiusmod tempor incididunt ut labore et dolore magna aliqua.</p><p>Lorem ipsum dolor sit amet, consectetur adipiscing elit, sed do eiusmod tempor incididunt ut labore et dolore magna aliqua.</p></div>
  </div>

  <div class="footer-line"></div>
  <div class="footer-text">Presentation Title | 2</div>
  <div class="brand"><i></i>VELTRANO</div>
</section>

<!-- Assumptions / Dependencies / Risks -->
<section class="slide s6">
  <div class="bar"></div>
  <div class="slide-title">Assumptions / Dependencies / Risks</div>

  <div class="col" style="left:34px">
    <svg viewBox="0 0 30 30"><circle cx="15" cy="15" r="15" fill="var(--gold)"/><g fill="none" stroke="#fff" stroke-width="1.2"><path d="M15 6 L24 22 H6 Z"/><path d="M15 11 v6 M15 19 v1"/></g></svg>
    <div class="label">Risks</div>
    <ul class="rows">
      <li><b>Critical</b><i style="background:var(--red)"></i><em>2</em></li>
      <li><b>High</b><i style="background:var(--green)"></i><em>5</em></li>
      <li><b>Moderate</b><i style="background:var(--amber)"></i><em>3</em></li>
      <li><b>Low</b><i style="background:var(--blue)"></i><em>1</em></li>
      <li><b>Negligible</b><i style="background:var(--grey)"></i><em>1</em></li>
    </ul>
    <div class="note">Lorem ipsum dolor sit amet, consectetur adipiscing elit, sed do eiusmod tempor incididunt ut labore et dolore magna aliqua.</div>
  </div>
  <div class="col" style="left:158px">
    <svg viewBox="0 0 30 30"><circle cx="15" cy="15" r="15" fill="var(--gold)"/><g fill="none" stroke="#fff" stroke-width="1.2"><circle cx="15" cy="13" r="6"/><path d="M11 18 v5 h6 M13 11 q2-2 4 0 q0 2-2 3"/></g></svg>
    <div class="label">Assumptions</div>
    <ul class="rows">
      <li><b>Critical</b><i style="background:var(--red)"></i><em>2</em></li>
      <li><b>High</b><i style="background:var(--green)"></i><em>5</em></li>
      <li><b>Moderate</b><i style="background:var(--amber)"></i><em>3</em></li>
      <li><b>Low</b><i style="background:var(--blue)"></i><em>1</em></li>
      <li><b>Negligible</b><i style="background:var(--grey)"></i><em>1</em></li>
    </ul>
    <div class="note">Lorem ipsum dolor sit amet, consectetur adipiscing elit, sed do eiusmod tempor incididunt ut labore et dolore magna aliqua.</div>
  </div>
  <div class="col" style="left:283px">
    <svg viewBox="0 0 30 30"><circle cx="15" cy="15" r="15" fill="var(--gold)"/><g fill="none" stroke="#fff" stroke-width="1.2"><rect x="14" y="7" width="9" height="12"/><path d="M16 10 h5 M16 13 h5 M16 16 h3 M7 23 l4-8 l4 8"/></g></svg>
    <div class="label">Issues</div>
    <ul class="rows">
      <li><b>Critical</b><i style="background:var(--red)"></i><em>2</em></li>
      <li><b>High</b><i style="background:var(--green)"></i><em>5</em></li>
      <li><b>Moderate</b><i style="background:var(--amber)"></i><em>3</em></li>
      <li><b>Low</b><i style="background:var(--blue)"></i><em>1</em></li>
      <li><b>Negligible</b><i style="background:var(--grey)"></i><em>1</em></li>
    </ul>
    <div class="note">Lorem ipsum dolor sit amet, consectetur adipiscing elit, sed do eiusmod tempor incididunt ut labore et dolore magna aliqua.</div>
  </div>
  <div class="col" style="left:407px">
    <svg viewBox="0 0 30 30"><circle cx="15" cy="15" r="15" fill="var(--gold)"/><g fill="none" stroke="#fff" stroke-width="1.2"><path d="M8 8 h7 l-2-2 M15 8 l-2 2 M8 23 l6-8 l3 3 l5-8 M20 10 h3 v3"/></g></svg>
    <div class="label">Dependencies</div>
    <ul class="rows">
      <li><b>Critical</b><i style="background:var(--red)"></i><em>2</em></li>
      <li><b>High</b><i style="background:var(--green)"></i><em>5</em></li>
      <li><b>Moderate</b><i style="background:var(--amber)"></i><em>3</em></li>
      <li><b>Low</b><i style="background:var(--blue)"></i><em>1</em></li>
      <li><b>Negligible</b><i style="background:var(--grey)"></i><em>1</em></li>
    </ul>
    <div class="note">Lorem ipsum dolor sit amet, consectetur adipiscing elit, sed do eiusmod tempor incididunt ut labore et dolore magna aliqua.</div>
  </div>

  <div class="footer-line"></div>
  <div class="footer-text">Presentation Title | 2</div>
  <div class="brand"><i></i>VELTRANO</div>
</section>

</body>
</html>
```